CEDAR PEAK HEATING AND COOLING

Industry/Entity Type

Hvac

Requirements
Must have
• logo
My name: Tom Brennerov
Phone number 905-334-6071
Text:
Furnace and AC repairs
New furnace and AC installation
Ductwork
Gas lines
Water Tanks
Tankless water heaters
Nice to have
• Profesional modern look

```html
<!DOCTYPE html>
<html lang="en">
<head>
<meta charset="utf-8">
<title>Cedar Peak Heating and Cooling – Business Card</title>
<link href="https://fonts.googleapis.com/css2?family=Arimo:wght@400;700&display=swap" rel="stylesheet">
<style>
  :root {
    --page-bg: #e9e7e3;
    --card-bg: #f4f3f0;
    --card-edge: #d2d0cb;
    --navy: #1c3570;
    --band-blue: #23468a;
    --band-text: #e6dccb;
    --service-text: #1f2f5c;
    --bullet-red: #b3232c;
  }
  * { margin: 0; padding: 0; box-sizing: border-box; }
  html, body {
    width: 1200px;
    height: 970px;
    overflow: hidden;
    background: var(--page-bg);
    font-family: "Arimo", Arial, sans-serif;
  }
  .business-card {
    position: absolute;
    left: 80px;
    top: 175px;
    width: 1040px;
    height: 620px;
    background: var(--card-bg);
    border: 1px solid var(--card-edge);
    box-shadow: 0 10px 30px rgba(0,0,0,0.12);
  }
  .brand {
    position: absolute;
    left: 0;
    right: 0;
    top: 150px;
    display: flex;
    align-items: center;
    justify-content: center;
    gap: 34px;
  }
  .brand-mark {
    width: 110px;
    height: 110px;
    border-radius: 50%;
    background: var(--navy);
    flex: none;
  }
  .brand-name {
    color: var(--navy);
    font-weight: 700;
    font-size: 50px;
    line-height: 1.1;
    letter-spacing: 1px;
  }
  .contact-band {
    position: absolute;
    left: 0;
    right: 0;
    top: 370px;
    height: 95px;
    background: var(--band-blue);
    color: var(--band-text);
    text-align: center;
  }
  .contact-name {
    margin-top: 10px;
    font-size: 34px;
    font-weight: 700;
    letter-spacing: 1px;
    text-transform: uppercase;
  }
  .contact-phone {
    margin-top: 6px;
    font-size: 22px;
    display: inline-flex;
    align-items: center;
    gap: 10px;
  }
  .phone-icon { width: 22px; height: 22px; }
  .service-list {
    position: absolute;
    top: 495px;
    list-style: none;
    color: var(--service-text);
    font-size: 21px;
    line-height: 35px;
  }
  .service-list li { display: flex; align-items: center; gap: 12px; }
  .service-list li::before,
  .service-list.right li::after {
    content: "";
    width: 8px;
    height: 8px;
    border-radius: 50%;
    background: var(--bullet-red);
    flex: none;
  }
  .service-list.left { left: 32px; }
  .service-list.right { right: 32px; text-align: right; }
  .service-list.right li { justify-content: flex-end; }
  .service-list.right li::before { display: none; }
</style>
</head>
<body>
  <main class="business-card">
    <header class="brand">
      <span class="brand-mark"></span>
      <div class="brand-name">CEDAR PEAK<br>HEATING AND COOLING</div>
    </header>

    <section class="contact-band">
      <p class="contact-name">Tom Brennerov</p>
      <p class="contact-phone">
        <svg class="phone-icon" viewBox="0 0 24 24" aria-hidden="true">
          <path fill="currentColor" d="M3 8c0-2 3-4 9-4s9 2 9 4v2h-4V8.5c-1-.6-3-1-5-1s-4 .4-5 1V10H3z M6 11h12l2 8H4z M12 13a2.5 2.5 0 1 0 0 5a2.5 2.5 0 1 0 0-5z"/>
        </svg>
        905-334-6071
      </p>
    </section>

    <ul class="service-list left">
      <li>Gas lines</li>
      <li>Ductwork</li>
      <li>Water Tanks</li>
    </ul>
    <ul class="service-list right">
      <li>Tankless water heaters</li>
      <li>Furnace and AC repairs</li>
      <li>New furnace and AC installation</li>
    </ul>
  </main>
</body>
</html>
```